Morrow Family Reunion Flyer

A flyer detailing family reunion events. It should be complimentary to the logo style and fonts. BE DIFFERENT AVOID TEMPLATES

The 2015 Morrow Family Reunion
Descendants of Tobias Elwin Harold Morrow

Friday August 14th 2pm
Jummah Prayer At Sunvale Mosque
Followed by Family Get Together

Saturday august 15th 12pm
Family Reunion Picnic
4123 morrow Dr.
bowie

Hosted by the Children of The Prestigious Morrow Family

Colors
0355a3
9bcb3c

Requirements
Must have
• Logo

```html
<!DOCTYPE html>
<html lang="en">
<head>
<meta charset="utf-8">
<title>The 2015 Morrow Family Reunion</title>
<link rel="stylesheet" href="https://fonts.googleapis.com/css2?family=Libre+Baskerville:wght@400;700&family=Open+Sans:wght@600;700&display=swap">
<style>
  :root {
    --green: #13803a;
    --blue: #3a9fdc;
    --parchment-light: #fdf6d2;
    --parchment-mid: #f6e7ad;
    --parchment-edge: #efd891;
    --tree-blue-top: rgba(58, 159, 220, 0.22);
    --tree-blue-bottom: rgba(58, 159, 220, 0.10);
    --tree-green-top: rgba(19, 128, 58, 0.20);
    --tree-green-bottom: rgba(19, 128, 58, 0.08);
  }
  * { margin: 0; padding: 0; box-sizing: border-box; }
  html, body { width: 1200px; height: 846px; overflow: hidden; background: #ffffff; }
  .flyer {
    position: relative;
    width: 1200px;
    height: 846px;
    overflow: hidden;
    background: radial-gradient(ellipse at 45% 40%, var(--parchment-light) 0%, var(--parchment-mid) 65%, var(--parchment-edge) 100%);
    font-family: "Libre Baskerville", Georgia, serif;
  }
  .tree { position: absolute; }
  .tree--left {
    left: 0; top: 235px; width: 230px; height: 611px;
    border-radius: 0 115px 0 0;
    background: linear-gradient(180deg, var(--tree-blue-top) 0%, var(--tree-blue-bottom) 100%);
  }
  .tree--right {
    left: 880px; top: 52px; width: 320px; height: 794px;
    border-radius: 160px 0 0 0;
    background: linear-gradient(180deg, var(--tree-green-top) 0%, var(--tree-green-bottom) 100%);
  }
  .brand-mark {
    position: absolute;
    left: 20px; top: 14px;
    width: 184px; height: 184px;
    border: 5px solid var(--green);
    border-radius: 50%;
  }
  .brand-name {
    position: absolute;
    left: 14px; top: 206px;
    font-family: "Open Sans", Arial, sans-serif;
    font-weight: 700;
    font-size: 12px;
    line-height: 16px;
    color: var(--green);
  }
  .title {
    position: absolute;
    left: 205px; top: 14px;
    font-size: 46px;
    line-height: 60px;
    font-weight: 700;
    color: var(--green);
    white-space: nowrap;
  }
  .subtitle {
    position: absolute;
    left: 218px; top: 78px;
    font-family: "Open Sans", Arial, sans-serif;
    font-size: 31px;
    line-height: 42px;
    font-weight: 600;
    color: var(--blue);
    white-space: nowrap;
  }
  .event { position: absolute; white-space: nowrap; }
  .event--friday { left: 172px; top: 274px; font-size: 29px; line-height: 43px; color: var(--green); }
  .event--saturday { right: 115px; top: 498px; font-size: 30px; line-height: 47px; color: var(--blue); text-align: right; }
  .hosts {
    position: absolute;
    left: 95px; top: 780px;
    font-size: 31px;
    line-height: 42px;
    font-weight: 700;
    white-space: nowrap;
    color: var(--blue);
  }
  .hosts__family { color: var(--green); }
</style>
</head>
<body>
<main class="flyer">
  <div class="tree tree--left" role="img" aria-label="Blue line illustration of a tall tree"></div>
  <div class="tree tree--right" role="img" aria-label="Green line illustration of a tall leafy tree"></div>

  <div class="brand-mark"></div>
  <p class="brand-name">Morrow Family Reunion 2015</p>

  <h1 class="title">The 2015 Morrow Family Reunion</h1>
  <h2 class="subtitle">Descendants of Tobias Elwin Harold Morrow</h2>

  <section class="event event--friday">
    <p>Friday August 14th 2pm</p>
    <p>Jummah Prayer At Sunvale Mosque</p>
    <p>Followed by Family Get Together</p>
  </section>

  <section class="event event--saturday">
    <p>Saturday august 15th 12pm</p>
    <p>Family Reunion Picnic</p>
    <p>4123 morrow Dr.</p>
    <p>bowie</p>
  </section>

  <p class="hosts">Hosted by the Children of <span class="hosts__family">The Prestigious Morrow Family</span></p>
</main>
</body>
</html>
```